New Business Card Design for Business Consulting Business

We need a business card design that reflects the simplicity of our business. We partner with our clients to help them deliver change. We are a different kind of business consulting group. We don't just provide you with the theory. We provide you with the leadership and capability to execute change.

Vonduro is a professional services organisation that partners with their clients to lead the execution of strategic process and system improvement initiatives. Vonduro combines hands on delivery with coaching in best practice methodologies and approaches to build their clients capabilities to ensure their ongoing success in project implementations. Vonduro offers business advisory services in Project Management, Business Process Management, Change Management and Business Analytics.

Reason: Hi Designers, Thanks for all of your great designs. There are some really creative and cool ideas. Everyone is really capturing the essence of my business Vonduro. I am extending the deadline for the business card design by 6 days as I need to consult my Marketing colleague who won't be back in Australia until Wednesday. I would like to sit down with them and review all of the best designs. The key themes of the things I have really liked on my first review are: 1) Capturing the company website on the back of the card. 2) Including the company logo on the back of the card too. 3) Including the types of services on the back of the card that the company offers - Project Management - Business Process Management - Change Management - Business Analytics 4) Utilising some images on the back of the card Just so everyone knows the colour palette for the Vonduro company logo is: R: 0 G: 86 B: 162 or C: 97% M: 73% Y: 4% K: 0% Thanks Gareth

Hi Designers,

Thanks for all of your submissions to date.  I am working through each design and will provide feedback on all the great work.

One thing I would like to ask is if you could submit a version that has my academic credentials under or after my name.  I am not a big fan of doing this but as I am in business consulting it does seem to be quite common.

I hold a Bachelor of Commerce (BCom) and a Master of Business Administration (MBA)

Thanks

Gareth

Hi Designers,

Thanks for all of your fantastic designs.  There are some really great designs here for my business.  I am still in the process of reviewing designs and should have this completed by tomorrow.  Some of the things I have learnt from this round of designs are:

1) I prefer to have the card without my academic qualifications

2) I really like cards that have a blue back

3) I prefer to have my name and title either left or right of centre

I hope this helps and I will endeavour to get through all of the designs tomorrow

Cheers

Gareth

Target Market(s)

We target large corporate organisations

Industry/Entity Type

Leadership

Requirements
Must have
• Must have the following business details

Gareth Pilling - Director
Address: Level 7, 82 Harlow Street, Melbourne, Australia, 3000
Phone: +61 3 527 840 213
Fax: +61 3 9214 5037
Email: gareth.pilling@vonduro-example.com.au
LinkedIn: au.linkedin.com/in/garethjpilling/
Twiiter: @garethjpilling
Website: www.vonduro-example.com.au

```html
<!DOCTYPE html>
<html lang="en">
<head>
<meta charset="utf-8">
<title>Vonduro Business Card</title>
<link rel="stylesheet" href="https://fonts.googleapis.com/css2?family=Montserrat:wght@300;400;500&display=swap">
<style>
  :root {
    --backdrop: #9b9598;
    --card: #1d1d1e;
    --ink: #e6e6e6;
    --ink-soft: #a9a9a9;
  }
  * { margin: 0; padding: 0; box-sizing: border-box; }
  html, body {
    width: 1200px;
    height: 623px;
    overflow: hidden;
    background: var(--backdrop);
    font-family: "Montserrat", Arial, sans-serif;
  }
  .stage {
    width: 1200px;
    height: 623px;
    display: flex;
    align-items: center;
    justify-content: center;
    gap: 60px;
  }
  .card {
    width: 500px;
    height: 306px;
    background: var(--card);
    color: var(--ink);
    border-radius: 3px;
    position: relative;
  }
  /* Contact side */
  .card--details {
    display: flex;
    flex-direction: column;
    align-items: center;
    padding-top: 42px;
    text-align: center;
  }
  .holder-name {
    font-size: 16px;
    font-weight: 500;
    letter-spacing: 0.32em;
    text-transform: uppercase;
  }
  .holder-title {
    margin-top: 6px;
    font-size: 8px;
    font-weight: 400;
    letter-spacing: 0.3em;
    text-transform: uppercase;
    color: var(--ink-soft);
  }
  .contact-list {
    list-style: none;
    margin-top: 26px;
    font-size: 9px;
    font-weight: 300;
    letter-spacing: 0.08em;
    line-height: 22px;
  }
  /* Brand side */
  .card--brand {
    display: flex;
    align-items: center;
    justify-content: center;
    overflow: hidden;
  }
  .brand {
    display: flex;
    flex-direction: column;
    align-items: flex-end;
  }
  .brand-name {
    font-size: 64px;
    font-weight: 400;
    letter-spacing: 0.01em;
    line-height: 1;
    color: var(--ink);
  }
  .brand-suffix {
    margin-top: 6px;
    font-size: 10px;
    font-weight: 400;
    letter-spacing: 0.05em;
    color: var(--ink);
  }
</style>
</head>
<body>
<main class="stage">
  <section class="card card--details">
    <h1 class="holder-name">Gareth Pilling</h1>
    <p class="holder-title">Director</p>
    <ul class="contact-list">
      <li>Phone: +61 3 527 840 213</li>
      <li>Fax: +61 3 9214 5037</li>
      <li>Email: gareth.pilling@vonduro-example.com.au</li>
      <li>LinkedIn: au.linkedin.com/in/garethjpilling/</li>
      <li>Twitter: @garethjpilling</li>
      <li>Website: www.vonduro-example.com.au</li>
      <li>Level 7, 82 Harlow Street, Melbourne, Australia, 3000</li>
    </ul>
  </section>

  <section class="card card--brand">
    <div class="brand">
      <span class="brand-name">Vonduro</span>
      <span class="brand-suffix">Pty Ltd</span>
    </div>
  </section>
</main>
</body>
</html>
```